Law firm Seeks Modern and Engaging Site Redesign

Law firm seeks a new web site. Should be modern, but retaining existing logo. Needs to include contact section, professional bio, services offered, and contact information.

The site should be modern, responsive, and able to be SEO optimized.

The finished product should be coded in a Wordpress site, which I will provide. I can work with other platforms, including Wix, but WP is preferred.

Note the current site is https://www.tallowfieldlaw.example/#/home

Target Market(s)

Family Law Practice

Industry/Entity Type

Legal

Coding

Coded - Design and coding required

Number of Pages Required

4 page

Font styles to use
Sans Serif

Requirements
Must have
• Service description
Bio pages for partners
Contact Form
Awards/Publication page

```html
<!DOCTYPE html>
<html lang="en">
<head>
<meta charset="utf-8">
<title>Tallowfield Law</title>
<link href="https://fonts.googleapis.com/css2?family=Montserrat:wght@400;600;700;800&family=Open+Sans:wght@400;600&display=swap" rel="stylesheet">
<style>
:root{
  --blue:#3b7be0;
  --blue-dark:#1f3d8f;
  --navy:#173a7a;
  --ink:#222;
  --muted:#777;
  --light:#f3f3f3;
  --footer:#1b1b1b;
  --footer-bottom:#121212;
  --white:#fff;
}
*{margin:0;padding:0;box-sizing:border-box}
html,body{width:1200px;height:3096px;overflow:hidden}
body{font-family:"Open Sans",Arial,sans-serif;color:var(--ink);background:var(--white);position:relative}
.hero{position:absolute;left:0;top:0;width:1200px;height:640px;background:linear-gradient(160deg,#3a4048 0%,#6b6e70 40%,#c8c4bd 75%,#8d7a62 100%)}
.hero-photo{position:absolute;inset:0}
.navbar{position:absolute;left:220px;top:12px;width:760px;height:64px;background:var(--white);display:flex;align-items:center;justify-content:space-between;padding:0 20px}
.brand{font-family:Montserrat,sans-serif;font-weight:700;font-size:20px;color:var(--navy);display:flex;align-items:center;gap:10px}
.brand-square{width:14px;height:14px;background:var(--navy)}
.nav-links{display:flex;gap:22px;font-family:Montserrat,sans-serif;font-size:11px;font-weight:600;color:#333;align-items:center}
.social{display:flex;gap:6px;margin-left:6px}
.social span{width:20px;height:20px;background:var(--blue);display:block}
.hero-title{position:absolute;left:0;width:1200px;top:370px;text-align:center;color:var(--white);font-family:Montserrat,sans-serif;font-size:64px;font-weight:800;letter-spacing:4px;line-height:1}
.hero-title .thin{display:block;font-weight:400;font-size:46px;letter-spacing:6px;margin-top:4px}
.btn{display:inline-block;background:var(--blue);color:var(--white);font-family:Montserrat,sans-serif;font-weight:600;font-size:14px;letter-spacing:1px;padding:14px 26px;border-radius:3px}
.hero .btn{position:absolute;left:532px;top:524px}
.split{position:absolute;left:48px;width:1110px;display:flex;gap:40px;align-items:flex-start}
.photo{background:linear-gradient(180deg,#dfe7ee,#8ea3b6 60%,#5a6573)}
.section-title{font-family:Montserrat,sans-serif;font-weight:700;font-size:32px;letter-spacing:3px;color:var(--navy)}
.section-title .amp{color:#d8a23a}
.eyebrow{font-family:Montserrat,sans-serif;font-size:11px;font-weight:600;letter-spacing:2px;color:var(--muted);margin:6px 0 20px}
.body-text{font-size:14px;line-height:24px;color:#555}
.companies{top:720px}
.companies .photo{width:512px;height:260px;flex:none}
.people{top:1060px}
.people .text{text-align:right;width:570px}
.people .photo{width:500px;height:260px;flex:none;background:linear-gradient(180deg,#c9ccd0,#8b8f95 55%,#3a3e45)}
.plain-badge{display:inline-block;width:112px;height:48px;background:#2b2b2b;border-bottom:8px solid #e57a1e;margin-top:16px}
.services{position:absolute;left:0;top:1480px;width:1200px;height:520px;background:var(--light);text-align:center;padding-top:50px}
.kicker{font-family:Montserrat,sans-serif;font-size:13px;font-weight:600;color:var(--blue);letter-spacing:2px}
.center-title{font-family:Montserrat,sans-serif;font-weight:800;font-size:36px;letter-spacing:3px;color:var(--ink);margin-top:6px}
.center-sub{font-size:11px;color:var(--muted);letter-spacing:1px;margin-top:6px;font-family:Montserrat,sans-serif}
.service-row{display:flex;justify-content:center;gap:36px;margin-top:70px}
.service-card{width:168px;height:150px;background:var(--white);border:2px solid #c8d4ea;display:flex;flex-direction:column;align-items:center;justify-content:center;gap:14px}
.service-card span{font-family:Montserrat,sans-serif;font-size:12px;font-weight:700;color:var(--navy);letter-spacing:1px}
.services .btn{margin-top:60px}
.achieve{position:absolute;left:0;top:2070px;width:1200px;text-align:center}
.badge-row{display:flex;justify-content:center;gap:20px}
.badge-row.r1{margin-top:60px}
.badge-row.r2{margin-top:40px}
.badge-row.r3{margin-top:48px;gap:40px}
.b1{width:116px;height:40px;background:#2e2e2e;border-top:6px solid #c89a2e}
.b2{width:110px;height:64px;background:#2b2b2b;border-bottom:10px solid #e57a1e}
.b3{width:104px;height:104px;border-radius:50%;background:#2d3a6a;border:6px solid #c9a235}
.b3.alt{background:#efe9d4;border-color:#c9a235}
.help{position:absolute;left:0;top:2620px;width:1200px;height:144px;background:linear-gradient(90deg,var(--blue-dark),var(--blue));color:var(--white);display:flex;align-items:center;justify-content:space-between;padding:0 220px}
.help h3{font-family:Montserrat,sans-serif;font-size:20px;font-weight:700;letter-spacing:1px}
.help p{font-size:12px;margin-top:4px;opacity:.9}
.btn-outline{border:2px solid var(--white);color:var(--white);font-family:Montserrat,sans-serif;font-weight:600;font-size:12px;letter-spacing:1px;padding:10px 26px}
.footer{position:absolute;left:0;top:2764px;width:1200px;height:300px;background:var(--footer);display:flex;gap:60px;padding:50px 220px 0;color:#aaa;font-size:11px;line-height:18px}
.footer .col{width:220px}
.footer h4{font-family:Montserrat,sans-serif;color:var(--white);font-size:15px;font-weight:600;margin-bottom:14px}
.footer .brand{color:var(--white);font-size:17px;margin-bottom:14px}
.footer .brand-square{background:var(--white)}
.footer a{color:var(--blue)}
.post{margin-bottom:14px}
.post .date{color:#777;font-size:10px}
.footer-bottom{position:absolute;left:0;top:3064px;width:1200px;height:32px;background:var(--footer-bottom);color:#777;font-size:10px;display:flex;align-items:center;justify-content:space-between;padding:0 220px}
</style>
</head>
<body>

<header class="hero">
  <div class="hero-photo" role="img" aria-label="Two people shaking hands over a desk with a judge's gavel in the foreground"></div>
  <nav class="navbar">
    <div class="brand"><span class="brand-square"></span>Tallowfield Law</div>
    <div class="nav-links">
      <span>HOME</span><span>ABOUT</span><span>OUR SERVICES</span><span>OUR CLIENTS</span><span>CONTACT US</span>
      <div class="social"><span></span><span></span></div>
    </div>
  </nav>
  <h1 class="hero-title">WE FIGHT<span class="thin">FOR YOU</span></h1>
  <span class="btn">CONTACT US</span>
</header>

<section class="split companies">
  <div class="photo" role="img" aria-label="Business people walking through a glass-walled office lobby"></div>
  <div class="text">
    <h2 class="section-title">COMPANIES <span class="amp">&amp;</span> ORGANISATIONS</h2>
    <p class="eyebrow">TRUSTED FAMILY LAWYER</p>
    <p class="body-text">The team at Tallowfield Law is based in the heart of the city and has advised companies, charities and public bodies for many years. We guide boards through disputes, contracts and restructuring with the same care we give every family client, and we stay close from the first call to the final agreement.</p>
  </div>
</section>

<section class="split people">
  <div class="text">
    <h2 class="section-title">PEOPLE</h2>
    <p class="eyebrow">FAMILY FOCUSED ADVOCATES</p>
    <p class="body-text">Our partners founded the firm after two decades in family courts across the region. They have led custody, divorce and support matters of every size, and both are recognised by their peers each year. Together they bring calm judgement, clear advice and steady representation to clients facing the hardest moments of family life.</p>
    <span class="plain-badge"></span>
  </div>
  <div class="photo" role="img" aria-label="The two founding partners standing in the firm's office"></div>
</section>

<section class="services">
  <p class="kicker">WHAT WE DO</p>
  <h2 class="center-title">OUR SERVICES</h2>
  <p class="center-sub">OUR FIRM ACCEPTS ALL KINDS OF FAMILY LAW MATTERS</p>
  <div class="service-row">
    <div class="service-card">
      <svg width="56" height="56" viewBox="0 0 56 56" fill="none" stroke="#3b7be0" stroke-width="2"><circle cx="18" cy="14" r="6"/><circle cx="38" cy="14" r="6"/><path d="M8 44V28q0-6 10-6t10 6v16M28 44V28q0-6 10-6t10 6v16"/><path d="M28 8v40" stroke-dasharray="3 3"/></svg>
      <span>DIVORCE</span>
    </div>
    <div class="service-card">
      <svg width="56" height="56" viewBox="0 0 56 56" fill="none" stroke="#3b7be0" stroke-width="2"><circle cx="16" cy="12" r="6"/><circle cx="40" cy="12" r="6"/><circle cx="28" cy="30" r="4"/><path d="M8 48V26q0-6 8-6t8 6v22M32 48V26q0-6 8-6t8 6v22M24 48V40q0-4 4-4t4 4v8"/></svg>
      <span>CHILD CUSTODY</span>
    </div>
    <div class="service-card">
      <svg width="56" height="56" viewBox="0 0 56 56" fill="none" stroke="#3b7be0" stroke-width="2"><circle cx="28" cy="14" r="7"/><path d="M16 36q12-10 24 0"/><path d="M6 40h10l8 6h14l12-8M6 48h8"/></svg>
      <span>CHILD SUPPORT</span>
    </div>
    <div class="service-card">
      <svg width="56" height="56" viewBox="0 0 56 56" fill="none" stroke="#3b7be0" stroke-width="2"><rect x="8" y="16" width="40" height="26" rx="2"/><circle cx="28" cy="29" r="6"/><path d="M14 22h4M38 36h4"/></svg>
      <span>ALIMONY</span>
    </div>
  </div>
  <span class="btn">SEE MORE SERVICES</span>
</section>

<section class="achieve">
  <p class="kicker">WHAT WE ACHIEVE</p>
  <h2 class="center-title">OUR ACHIEVEMENT</h2>
  <p class="center-sub">PUBLICATIONS AND AWARDS</p>
  <div class="badge-row r1"><span class="b1"></span><span class="b1"></span><span class="b1"></span><span class="b1"></span><span class="b1"></span></div>
  <div class="badge-row r2"><span class="b2"></span><span class="b2"></span><span class="b2"></span><span class="b2"></span><span class="b2"></span></div>
  <div class="badge-row r3"><span class="b3"></span><span class="b3"></span><span class="b3"></span><span class="b3 alt"></span><span class="b3 alt"></span></div>
</section>

<section class="help">
  <div>
    <h3>LET US HELP YOU</h3>
    <p>Do you have any questions about our program? Don't hesitate to call us.</p>
  </div>
  <span class="btn-outline">SEND INQUIRIES</span>
</section>

<footer class="footer">
  <div class="col">
    <div class="brand"><span class="brand-square"></span>Tallowfield Law</div>
    <p>Tallowfield Law offers family law guidance with care and discretion for every client we serve.</p>
    <p style="margin-top:10px"><a>Read More</a></p>
  </div>
  <div class="col">
    <h4>Recent Posts</h4>
    <div class="post"><a>Preparing for your first custody hearing</a><div class="date">March 12, 2019</div></div>
    <div class="post"><a>What to bring to a divorce consultation</a><div class="date">March 04, 2019</div></div>
  </div>
  <div class="col">
    <h4>Latest Updates</h4>
    <div class="post"><a>@tallowfieldlaw</a> New guide on child support changes this year<div class="date">2 days ago</div></div>
    <div class="post"><a>@tallowfieldlaw</a> Thank you to everyone at the family law forum<div class="date">5 days ago</div></div>
  </div>
</footer>
<div class="footer-bottom">
  <span>© 2019 Tallowfield Law. All rights reserved.</span>
  <span>Home &nbsp; Blog &nbsp; Contact</span>
</div>

</body>
</html>
```